Business card design needed

I run a Beautician studio (for 7 years now)
I offer
- Velmo Skin Glide
- Lumora Renew
- Nails
- Facials
- Manicure
- Foot Treatment
It might not be necessary to list all those treatments?
Maybe the link to the Website is sufficient?
I leave that up to you ...
(more info on www.BrowsAndBloomByMirela.com.au)
Velmo SkinGlide is our biggest success, It replaces waxing.
I would like to incorporate the logo into the Business Card.
We had many complaints regarding our old Business Cards as the Phone Number was to small.
On the backside, we would like a "your next Appointment" section.
Looking forward to you Design, cheers ... Mirela
Brows by Bloom by Mirela
14 Korrin Pde 3954 Carrowby
www.BrowsAndBloomByMirela.com.au
03 8142 6639

```html
<!DOCTYPE html>
<html lang="en">
<head>
<meta charset="utf-8">
<title>Velmo Skin Glide – Business Card</title>
<link href="https://fonts.googleapis.com/css2?family=Didact+Gothic&family=Open+Sans:wght@800&display=swap" rel="stylesheet">
<style>
  :root {
    --page: #e6e3de;
    --card-white: #ffffff;
    --card-shade: #e4e4e2;
    --gold-light: #f2c21a;
    --gold-mid: #d9a812;
    --gold-deep: #b88f0a;
    --orange: #e07b1a;
    --ink: #2b2b2b;
    --text-green: #2e9e3e;
    --text-gold: #c8941a;
    --box-fill: #e8ebe7;
    --box-edge: #d8dbd5;
    --web-grey: #f3edd6;
  }
  * { box-sizing: border-box; margin: 0; padding: 0; }
  html, body { width: 1200px; height: 900px; overflow: hidden; }
  body {
    background: var(--page);
    display: flex;
    flex-direction: column;
    align-items: center;
    justify-content: center;
    gap: 40px;
    font-family: "Didact Gothic", sans-serif;
  }
  .card {
    position: relative;
    width: 640px;
    height: 391px;
    border-radius: 22px;
    overflow: hidden;
    background: radial-gradient(ellipse at 30% 40%, var(--card-white) 40%, var(--card-shade) 100%);
    box-shadow: 0 6px 18px rgba(0,0,0,0.18);
  }
  .card__panel { position: absolute; inset: 0; width: 100%; height: 100%; }
  .brand {
    position: absolute;
    display: flex;
    align-items: center;
    gap: 12px;
  }
  .brand__dot {
    width: 34px; height: 34px; border-radius: 50%;
    background: var(--orange);
  }
  .brand__name {
    font-size: 28px;
    color: var(--ink);
    letter-spacing: 1px;
    white-space: nowrap;
  }
  /* back side */
  .card--back .brand { left: 70px; top: 110px; }
  .services {
    position: absolute;
    right: 26px; top: 34px;
    list-style: none;
    text-align: right;
    font-family: "Open Sans", sans-serif;
    font-weight: 800;
    font-size: 12.5px;
    line-height: 33px;
    color: var(--card-white);
    text-transform: uppercase;
    letter-spacing: 0.5px;
  }
  .appointment {
    position: absolute;
    left: 150px; top: 200px;
    width: 240px; height: 160px;
    background: var(--box-fill);
    border: 3px solid var(--box-edge);
    border-radius: 18px;
    padding: 14px 18px;
  }
  .appointment__title {
    font-family: "Open Sans", sans-serif;
    font-weight: 800;
    font-size: 12.5px;
    color: var(--ink);
    text-transform: uppercase;
    margin-bottom: 16px;
    white-space: nowrap;
  }
  .appointment__line { height: 1px; background: #555; margin-bottom: 30px; }
  /* front side */
  .card--front .brand { left: 60px; top: 55px; }
  .studio {
    position: absolute; left: 110px; top: 165px;
    font-size: 22px; color: var(--text-green);
    white-space: nowrap;
  }
  .contact {
    position: absolute; left: 100px; top: 245px;
    list-style: none;
    font-size: 20px; color: var(--text-gold);
  }
  .contact li { display: flex; align-items: center; gap: 10px; margin-bottom: 18px; white-space: nowrap; }
  .contact svg { width: 20px; height: 20px; fill: var(--text-gold); flex: none; }
  .website {
    position: absolute; right: 16px; top: 20px; height: 350px;
    writing-mode: vertical-rl;
    text-align: center;
    font-size: 15px; color: var(--web-grey);
  }
</style>
</head>
<body>

<section class="card card--back">
  <svg class="card__panel" viewBox="0 0 640 391" role="img" aria-label="Decorative flowing colour artwork in green, orange and gold">
    <defs>
      <linearGradient id="panelBack" x1="0" y1="0" x2="1" y2="1">
        <stop offset="0" stop-color="var(--gold-light)"/>
        <stop offset="1" stop-color="var(--gold-deep)"/>
      </linearGradient>
    </defs>
    <path d="M425,0 C390,120 405,260 470,391 L640,391 L640,0 Z" fill="url(#panelBack)"/>
  </svg>
  <div class="brand">
    <span class="brand__dot"></span>
    <span class="brand__name">Velmo Skin Glide</span>
  </div>
  <ul class="services">
    <li>Velmo Skin Glide</li>
    <li>Lumora Renew</li>
    <li>Nails</li>
    <li>Facials</li>
    <li>Manicure</li>
    <li>Foot Treatment</li>
  </ul>
  <div class="appointment">
    <p class="appointment__title">Your next appointment:</p>
    <div class="appointment__line"></div>
    <div class="appointment__line"></div>
    <div class="appointment__line"></div>
  </div>
</section>

<section class="card card--front">
  <svg class="card__panel" viewBox="0 0 640 391" role="img" aria-label="Decorative flowing colour artwork in green, orange and gold">
    <defs>
      <linearGradient id="panelFront" x1="0" y1="0" x2="1" y2="1">
        <stop offset="0" stop-color="var(--gold-light)"/>
        <stop offset="1" stop-color="var(--gold-deep)"/>
      </linearGradient>
    </defs>
    <path d="M400,0 C435,120 405,270 435,391 L640,391 L640,0 Z" fill="url(#panelFront)"/>
  </svg>
  <div class="brand">
    <span class="brand__dot"></span>
    <span class="brand__name">Velmo Skin Glide</span>
  </div>
  <p class="studio">Brows by Bloom by Mirela</p>
  <ul class="contact">
    <li>
      <svg viewBox="0 0 24 24" aria-hidden="true"><path d="M6.6 10.8a15.1 15.1 0 0 0 6.6 6.6l2.2-2.2a1 1 0 0 1 1-.25 11.4 11.4 0 0 0 3.6.57 1 1 0 0 1 1 1V20a1 1 0 0 1-1 1A17 17 0 0 1 3 4a1 1 0 0 1 1-1h3.5a1 1 0 0 1 1 1c0 1.25.2 2.45.57 3.57a1 1 0 0 1-.25 1z"/></svg>
      03 8142 6639
    </li>
    <li>
      <svg viewBox="0 0 24 24" aria-hidden="true"><path d="M12 3 2 12h3v8h5v-5h4v5h5v-8h3z"/></svg>
      14 Korrin Pde 3954 Carrowby
    </li>
  </ul>
  <p class="website">www.BrowsAndBloomByMirela.com.au</p>
</section>

</body>
</html>
```